First Aid Training business needs business card design

We would like a double sided business card designed for a first aid training business - Brindlewood First Aid. We provide first aid training and , WHS (work, health and safety) training.

The attached word document contains the key information we would like on each side of the business card.

Final design needs to be delivered in print ready format, along with the original file.

```html
<!DOCTYPE html>
<html lang="en">
<head>
<meta charset="UTF-8">
<title>Brindlewood First Aid – Business Card</title>
<link rel="stylesheet" href="https://fonts.googleapis.com/css2?family=Montserrat:wght@600&family=Poppins:wght@400;500;600&display=swap">
<style>
  :root {
    --card-black: #020202;
    --brand-red: #f10d0d;
    --deep-red: #a30000;
    --white: #ffffff;
    --soft-white: #e9e9e9;
    --ghost: #1b1b1b;
  }
  * { box-sizing: border-box; margin: 0; padding: 0; }
  html, body { width: 1200px; height: 1099px; overflow: hidden; }
  body {
    background: linear-gradient(180deg, #000 0%, #0c0000 45%, #5a0000 80%, var(--deep-red) 100%);
    font-family: "Poppins", sans-serif;
    color: var(--white);
    position: relative;
  }
  .card {
    position: absolute;
    left: 170px;
    width: 860px;
    height: 491px;
    background: var(--card-black);
    overflow: hidden;
  }
  .card--front { top: 38px; }
  .card--back { top: 570px; }

  /* Front */
  .front-brand {
    position: absolute;
    left: 183px;
    top: 208px;
    display: flex;
    align-items: center;
    gap: 22px;
  }
  .brand-dot {
    width: 62px; height: 62px;
    border-radius: 50%;
    background: var(--brand-red);
    flex: none;
  }
  .brand-name {
    font-family: "Montserrat", sans-serif;
    font-weight: 600;
    color: var(--white);
    letter-spacing: 0.5px;
  }
  .front-brand .brand-name { font-size: 34px; }
  .ghost-circle {
    position: absolute;
    left: 648px;
    top: 303px;
    width: 220px; height: 220px;
    border-radius: 50%;
    background: var(--ghost);
  }

  /* Back */
  .back-brand {
    position: absolute;
    left: 95px;
    top: 140px;
    width: 240px;
    text-align: center;
  }
  .back-brand .brand-dot { width: 58px; height: 58px; margin: 0 auto 20px; }
  .back-brand .brand-name { font-size: 27px; line-height: 1.2; }
  .divider {
    position: absolute;
    left: 429px; top: 80px;
    width: 3px; height: 292px;
    background: var(--white);
  }
  .contact-block { position: absolute; left: 465px; top: 80px; }
  .person-name { font-size: 22px; font-weight: 400; line-height: 1.2; }
  .person-name .first { color: var(--brand-red); font-weight: 600; }
  .person-role { font-size: 15px; color: var(--soft-white); margin-top: 2px; }
  .contact-list { list-style: none; margin-top: 65px; }
  .contact-list li {
    display: flex; align-items: center; gap: 6px;
    font-size: 15px; height: 27px; color: var(--soft-white);
  }
  .contact-list svg { width: 17px; height: 17px; flex: none; }
  .onsite { margin-top: 27px; font-size: 13px; line-height: 17.5px; color: var(--soft-white); }
  .onsite-title { color: var(--brand-red); font-weight: 600; letter-spacing: -0.2px; }
  .service-band {
    position: absolute;
    left: 0; top: 420px;
    width: 100%; height: 36px;
    background: var(--brand-red);
    display: flex; align-items: center; justify-content: center;
    font-size: 17px; font-weight: 600;
    letter-spacing: 6.2px;
    color: var(--white);
  }
</style>
</head>
<body>
  <section class="card card--front" aria-label="Business card front">
    <div class="ghost-circle"></div>
    <div class="front-brand">
      <span class="brand-dot"></span>
      <span class="brand-name">BRINDLEWOOD FIRST AID</span>
    </div>
  </section>

  <section class="card card--back" aria-label="Business card back">
    <div class="back-brand">
      <div class="brand-dot"></div>
      <div class="brand-name">BRINDLEWOOD<br>FIRST AID</div>
    </div>
    <div class="divider"></div>
    <div class="contact-block">
      <p class="person-name"><span class="first">DANIEL</span> HARTLEY</p>
      <p class="person-role">President</p>
      <ul class="contact-list">
        <li>
          <svg viewBox="0 0 20 20"><circle cx="10" cy="10" r="10" fill="var(--brand-red)"/><path d="M7 5.5l2 2-1 1.3c.6 1.3 1.6 2.3 2.9 2.9l1.3-1 2 2-1.2 1.6c-3.6-.4-6.9-3.7-7.3-7.3z" fill="#fff"/></svg>
          0412 386 520
        </li>
        <li>
          <svg viewBox="0 0 20 20"><circle cx="10" cy="10" r="10" fill="var(--brand-red)"/><rect x="5" y="6.5" width="10" height="7" fill="#fff"/><path d="M5 6.5l5 4 5-4" stroke="var(--brand-red)" stroke-width="1.2" fill="none"/></svg>
          help@brindlewoodfirstaid.com.au
        </li>
        <li>
          <svg viewBox="0 0 20 20"><circle cx="10" cy="10" r="10" fill="var(--brand-red)"/><g stroke="#fff" stroke-width="1.1" fill="none"><circle cx="10" cy="10" r="5"/><ellipse cx="10" cy="10" rx="2.2" ry="5"/><path d="M5 10h10"/></g></svg>
          brindlewoodfirstaid.com.au
        </li>
      </ul>
      <div class="onsite">
        <p class="onsite-title">Onsite Training – We can come to you</p>
        <p>·Time efficient</p>
        <p>·Cost effective</p>
        <p>·Minimise downtime for your team</p>
      </div>
    </div>
    <div class="service-band">FIRST AID TRAINING, WHS TRAINING</div>
  </section>
</body>
</html>
```